'WILD' eye catching Business Card Design / Logo for production company / TV host / adventurer

Hi there,

We are looking for a 'WILD' and exciting logo and double sided business card for our business "Bright Harbor Studios".

Marcus Thorley is an international television host, adventurer, author and inspirational public speaker.

We want to project Marcus' talents onto his business card.

We are looking for a business card design that can carry over onto letter heads, emails etc. We want a design that is 'WILD', different and exciting.

Feel free to check out Marcus' web site: www.brightharborstudios.example.nz to get a better understanding what he is about.

Please feel free to go completely 'WILD' on this project as we want something different with lots of WOW factors.

Thank you so much and we look forward to your designs.

We have a feeling that there will be many more designs in the near future.

Best regards,

the production team

We have added another task to the list.

If the winning designer can also provide us with a matching letterhead and email signature based on the same style of design as the business card.

Target Market(s)

People with passion.

Industry/Entity Type

Business

Requirements
Must have
• Bright Harbor Studios
Marcus Thorley
42 Ferndale Lane
Oakbridge 7420
New Zealand

Phone +64-(0)3-5527 046
Cell +64-(0)274-615 238

email: brightharbornz@example.com
www.brightharborstuios.example.nz
Nice to have
• A feature made out of the name 'Bright Harbor Studios'.

Marcus Thorley's name reasonably obvious.

All other details (except web site) can be quite small.

```html
<!DOCTYPE html>
<html lang="en">
<head>
<meta charset="utf-8">
<title>Bright Harbor Studios – Business Card</title>
<link rel="stylesheet" href="https://fonts.googleapis.com/css2?family=Indie+Flower&family=Montserrat:wght@800&display=swap">
<style>
  :root {
    --sand-light: #e9bd86;
    --sand-mid: #dcaa70;
    --sand-deep: #cf9a5e;
    --card-white: #ffffff;
    --ink-brown: #7a3810;
    --ink-soft: #8a4a1e;
    --title-white: #fbf7f0;
    --title-brown: #7b3f14;
    --label-white: #ffffff;
    --stripe-tiger: #c9832e;
    --stripe-water: #3fb3d6;
    --stripe-earth: #7d6a3e;
    --stripe-zebra: #c9c9c9;
    --stripe-leaf: #4fa83a;
    --stripe-fire: #c9531a;
  }
  * { box-sizing: border-box; margin: 0; padding: 0; }
  html, body { width: 1200px; height: 675px; overflow: hidden; }
  body { position: relative; font-family: "Indie Flower", cursive; }

  .backdrop {
    position: absolute; inset: 0;
    background: linear-gradient(160deg, var(--sand-light) 0%, var(--sand-mid) 55%, var(--sand-deep) 100%);
  }

  .brand-title {
    position: absolute; left: 0; width: 1200px; top: 40px;
    text-align: center;
    font-family: "Indie Flower", cursive;
    font-size: 76px; line-height: 74px;
    color: var(--title-brown);
  }

  .card-strip {
    position: absolute; left: 66px; top: 212px; width: 1070px; height: 218px;
    display: flex;
  }

  .card-front { position: relative; width: 358px; height: 218px; display: flex; }
  .stripe { flex: 1; height: 100%; }
  .stripe--tiger { background: var(--stripe-tiger); }
  .stripe--water { background: var(--stripe-water); }
  .stripe--earth { background: var(--stripe-earth); }
  .stripe--zebra { background: var(--stripe-zebra); }
  .stripe--leaf  { background: var(--stripe-leaf); }
  .stripe--fire  { background: var(--stripe-fire); }
  .front-name {
    position: absolute; left: 0; right: 0; top: 68px;
    text-align: center; color: var(--card-white);
    font-size: 42px; line-height: 44px;
  }

  .card-back {
    width: 356px; height: 218px; background: var(--card-white);
    position: relative; color: var(--ink-brown);
  }
  .holder-name {
    position: absolute; left: 0; right: 0; top: 40px;
    text-align: center; font-size: 29px; font-weight: 400;
    color: var(--ink-brown);
    text-shadow: 0 0 0.6px var(--ink-brown);
  }
  .web-address {
    position: absolute; left: 0; right: 0; top: 90px;
    text-align: center; font-size: 23px; color: var(--ink-soft);
  }
  .address, .contact {
    position: absolute; top: 153px; font-size: 14px; line-height: 15.5px;
    color: var(--ink-soft); font-style: normal;
  }
  .address { left: 16px; }
  .contact { right: 12px; text-align: right; }

  .side-label {
    position: absolute; top: 470px; width: 300px;
    text-align: center; color: var(--label-white);
    font-family: "Montserrat", sans-serif; font-weight: 800;
    font-size: 42px; letter-spacing: 1px;
  }
  .side-label--front { left: 65px; }
  .side-label--back-a { left: 452px; }
  .side-label--back-b { left: 810px; }
</style>
</head>
<body>
  <div class="backdrop" role="img" aria-label="Rippled desert sand texture"></div>

  <h1 class="brand-title">Bright Harbor<br>Studios</h1>

  <div class="card-strip">
    <section class="card-front">
      <div class="stripe stripe--tiger" role="img" aria-label="Tiger fur texture"></div>
      <div class="stripe stripe--water" role="img" aria-label="Rippling pool water texture"></div>
      <div class="stripe stripe--earth" role="img" aria-label="Cracked dry earth texture"></div>
      <div class="stripe stripe--zebra" role="img" aria-label="Zebra stripe texture"></div>
      <div class="stripe stripe--leaf" role="img" aria-label="Green leaf texture"></div>
      <div class="stripe stripe--fire" role="img" aria-label="Fire flames texture"></div>
      <p class="front-name">Bright Harbor<br>Studios</p>
    </section>

    <section class="card-back">
      <h2 class="holder-name">Marcus Thorley</h2>
      <p class="web-address">www.brightharborstudios.example.nz</p>
      <address class="address">42 Ferndale Lane<br>Oakbridge 7420<br>New Zealand</address>
      <p class="contact">Phone +64-(0)3-5527 046<br>Cell +64-(0)274-615 238<br>email: brightharbornz@example.com</p>
    </section>

    <section class="card-back">
      <h2 class="holder-name">Marcus Thorley</h2>
      <p class="web-address">www.brightharborstudios.example.nz</p>
      <address class="address">42 Ferndale Lane<br>Oakbridge 7420<br>New Zealand</address>
      <p class="contact">+64-(0)3-5527 046<br>+64-(0)274-615 238<br>brightharbornz@example.com</p>
    </section>
  </div>

  <p class="side-label side-label--front">FRONT</p>
  <p class="side-label side-label--back-a">BACK</p>
  <p class="side-label side-label--back-b">BACK</p>
</body>
</html>
```